its a new company based in Christchurch new Zealand building computers ,repairs, upgrades and anything computers for the general public,i like bright happy colours like yellows, greens reds anything that stands out and it needs to communicant trust and security towards my new company,i have no logo yet,

Target Market(s)

target market of all ages

Industry/Entity Type

Building

Contact Information for Business Card

Pixel Harbour Limited,ph-0274829315,email-brightnode47@mailvista.example,14c tamworth cl,kelvale

```html
<!DOCTYPE html>
<html lang="en">
<head>
<meta charset="utf-8">
<title>Pixel Harbour – Business Card</title>
<link rel="stylesheet" href="https://fonts.googleapis.com/css2?family=Audiowide&family=Exo+2:wght@500;600&family=Great+Vibes&family=Bree+Serif&display=swap">
<style>
  :root {
    --page-bg: #e9ebef;
    --navy: #1a2a7a;
    --royal: #2450c0;
    --sky: #3a7be0;
    --magenta: #b0196b;
    --plum: #7a1a78;
    --white: #ffffff;
    --gold: #f2c230;
    --stamp-ink: #3a3a3a;
    --stamp-paper: #f4f1ea;
  }
  * { margin: 0; padding: 0; box-sizing: border-box; }
  html, body {
    width: 1200px; height: 801px; overflow: hidden;
    background: var(--page-bg);
  }
  .card {
    position: absolute; left: 100px; top: 115px;
    width: 1000px; height: 570px; overflow: hidden;
    border-radius: 6px;
    background: linear-gradient(135deg, var(--navy) 0%, var(--royal) 55%, var(--sky) 100%);
    box-shadow: 0 10px 30px rgba(0,0,0,0.18);
    font-family: "Exo 2", sans-serif; color: var(--white);
  }
  .card-bands { position: absolute; inset: 0; width: 100%; height: 100%; }
  .brand-title {
    position: absolute; right: 40px; top: 30px;
    font-family: "Audiowide", sans-serif; font-weight: 400;
    font-size: 54px; line-height: 64px; letter-spacing: 2px;
  }
  .brand-row {
    position: absolute; left: 40px; top: 128px;
    display: flex; align-items: center; gap: 20px;
  }
  .brand-mark { width: 72px; height: 72px; background: var(--gold); border-radius: 8px; }
  .brand-name {
    font-family: "Audiowide", sans-serif; font-size: 40px; line-height: 48px; letter-spacing: 1px;
  }
  .product-visual {
    position: absolute; right: 40px; top: 118px; width: 320px; height: 210px;
    border-radius: 8px;
    background: linear-gradient(160deg, #2b2f3a 0%, #4a8fd8 45%, #1d2230 100%);
    opacity: 0.9;
  }
  .services {
    position: absolute; left: 60px; top: 222px; list-style: none;
    font-size: 28px; font-weight: 600; line-height: 40px;
  }
  .services li { display: flex; align-items: center; gap: 14px; }
  .services svg { width: 26px; height: 26px; }
  .guarantee {
    position: absolute; left: 60px; top: 358px; width: 270px; height: 76px;
    background: var(--stamp-paper); border: 3px double var(--stamp-ink);
    border-radius: 38px; color: var(--stamp-ink); text-align: center;
  }
  .guarantee-script { font-family: "Great Vibes", cursive; font-size: 24px; line-height: 28px; margin-top: 4px; }
  .guarantee-word { font-family: "Bree Serif", serif; font-size: 29px; letter-spacing: 3px; line-height: 34px; }
  .contact {
    position: absolute; right: 40px; top: 362px; text-align: right;
    font-size: 26px; font-weight: 500; line-height: 38px;
  }
  .address {
    position: absolute; left: 60px; bottom: 22px;
    font-size: 27px; font-weight: 500; line-height: 36px;
  }
</style>
</head>
<body>
  <section class="card">
    <svg class="card-bands" viewBox="0 0 1000 570" preserveAspectRatio="none" aria-hidden="true">
      <defs>
        <linearGradient id="band-magenta" x1="0" y1="0" x2="1" y2="1">
          <stop offset="0" stop-color="#7a1a78"/>
          <stop offset="1" stop-color="#c21e6e"/>
        </linearGradient>
      </defs>
      <polygon points="600,0 1000,0 1000,570 780,570" fill="url(#band-magenta)"/>
      <polygon points="600,0 650,0 830,570 780,570" fill="#3a6fd8" opacity="0.55"/>
    </svg>

    <h1 class="brand-title">PIXEL HARBOUR</h1>

    <div class="brand-row">
      <span class="brand-mark"></span>
      <span class="brand-name">PIXEL HARBOUR</span>
    </div>

    <div class="product-visual" role="img" aria-label="Desktop computer with monitor, tower, keyboard and mouse"></div>

    <ul class="services">
      <li><svg viewBox="0 0 24 24" fill="none" stroke="currentColor" stroke-width="3" stroke-linecap="round"><path d="M7 6.5a8 8 0 1 0 10 0"/><line x1="12" y1="3" x2="12" y2="11"/></svg>Building Computers</li>
      <li><svg viewBox="0 0 24 24" fill="none" stroke="currentColor" stroke-width="3" stroke-linecap="round"><path d="M7 6.5a8 8 0 1 0 10 0"/><line x1="12" y1="3" x2="12" y2="11"/></svg>Computer Repairs</li>
      <li><svg viewBox="0 0 24 24" fill="none" stroke="currentColor" stroke-width="3" stroke-linecap="round"><path d="M7 6.5a8 8 0 1 0 10 0"/><line x1="12" y1="3" x2="12" y2="11"/></svg>Computer Upgrades</li>
    </ul>

    <div class="guarantee">
      <div class="guarantee-script">100% Satisfaction</div>
      <div class="guarantee-word">GUARANTEED</div>
    </div>

    <div class="contact">
      <div>brightnode47@mailvista.example</div>
      <div>027 482 9315</div>
    </div>

    <div class="address">
      <div>Pixel Harbour Ltd</div>
      <div>14c Tamworth Cl, Kelvale</div>
    </div>
  </section>
</body>
</html>
```